Boutique Real Estate Brokerage Maplind Realty Website Design

Winning designer work on migrate as well through zip burrow.
We need a new website as an informational hub to aid our print and digital strategy as well as showing that we are located in Ashford Hill and Florida. I have a boutique real estate brokerage and advisory firm specializing in residential leasing, multifamily sales and 1031 Exchange appropriation. This won't be a portal to search properties, it will be a place for information. I'd like space for an ebook to be downloaded and information on my probate sales and multifamily leasing marketing campaigns. I included my logo and will leave it up to the designer to come up with colors to match it. I have also attached verbiage for each page. The final design should have a modern high end look that reflects gentrifying Ashford Hill as well as beautiful Florida.
Thank you!
Target Market(s)
Owners of income producing real estate and develop-able land in Ashford Hill, NY and Florida.
Industry/Entity Type
Real Estate
Coding
Coded - Design and coding required
Number of Pages Required
5+ page
Colors
Designer to choose colors to be used in the design.
Requirements
Must have
- A modern elegant look
Nice to have
- pictures of brooklyn and florida
Should not have
- real estate search pages

```html
<!DOCTYPE html>
<html lang="en">
<head>
<meta charset="utf-8">
<title>Maplind Realty</title>
<link href="https://fonts.googleapis.com/css2?family=Montserrat:wght@300;400;500;600;700&display=swap" rel="stylesheet">
<style>
:root{
  --ink:#0b0b0b;
  --white:#ffffff;
  --text:#555555;
  --muted:#777777;
  --line:#2a2a2a;
  --brick-a:#6b3b2c;
  --brick-b:#3a231b;
  --footer:#1f1f1f;
  --steel:#8a8a8a;
}
*{box-sizing:border-box;margin:0;padding:0}
html,body{width:1200px;height:2677px;overflow:hidden}
body{font-family:'Montserrat',sans-serif;color:var(--ink);background:var(--white);position:relative}
a{color:inherit;text-decoration:none}
ul{list-style:none}

.topbar{height:42px;background:var(--ink);color:#ddd;font-size:13px;font-weight:300;display:flex;justify-content:flex-end;align-items:center;padding-right:79px}
.topbar .item{display:flex;align-items:center;gap:10px;padding:0 16px}
.topbar .item + .item{border-left:1px solid #444}
.topbar svg{fill:#fff}

.header{height:93px;position:relative}
.brand{position:absolute;left:79px;top:26px;display:flex;align-items:center;gap:14px}
.brand .mark{width:40px;height:40px;background:var(--steel)}
.brand .name{font-size:20px;font-weight:600;letter-spacing:3px;color:#8a8a8a}
.nav{position:absolute;right:79px;top:28px;display:flex;align-items:center;font-size:13.5px;font-weight:400}
.nav a{padding:0 16px;line-height:40px}
.nav a.active{background:var(--ink);color:var(--white);border-radius:20px;padding:0 23px;margin-right:10px}
.nav .search{padding-left:22px;display:flex;align-items:center}

.hero{position:absolute;top:135px;left:0;width:1200px;height:542px;background:linear-gradient(120deg,#4a2b21 0%,var(--brick-a) 45%,#7b5443 70%,var(--brick-b) 100%)}
.hero .arrow{position:absolute;top:242px;width:52px;height:52px;border-radius:50%;background:rgba(0,0,0,.45);display:flex;align-items:center;justify-content:center}
.hero .arrow.prev{left:12px}.hero .arrow.next{right:12px}
.hero h1{position:absolute;right:79px;top:172px;text-align:right;color:var(--white);font-size:37px;font-weight:700;line-height:47px;text-shadow:0 2px 6px rgba(0,0,0,.5)}
.btn{display:inline-flex;align-items:center;justify-content:center;background:var(--ink);color:var(--white);border-radius:26px;font-size:18px;font-weight:400;height:52px}
.hero .btn{position:absolute;right:79px;top:336px;width:182px}

.welcome{position:absolute;top:677px;left:0;width:1200px;text-align:center}
.welcome .kicker{margin-top:63px;font-size:19px;font-weight:500}
.welcome h2{font-size:41px;font-weight:600;margin-top:4px;letter-spacing:.5px}
.welcome p{width:640px;margin:18px auto 0;font-size:13.5px;font-weight:300;color:var(--text);line-height:27px}
.welcome p + p{margin-top:11px}
.welcome .btn{margin-top:22px;width:182px}

.services{position:absolute;top:1146px;left:0;width:1200px;display:flex;gap:6px}
.tile{width:396px}
.tile .photo{height:312px}
.tile .label{height:73px;background:var(--ink);color:var(--white);display:flex;align-items:center;justify-content:center;font-size:18px;font-weight:400}
.photo.kitchen{background:linear-gradient(160deg,#e9e7e2,#c9b79a)}
.photo.building{background:linear-gradient(180deg,#8c8a86,#5c5955)}
.photo.aerial{background:linear-gradient(180deg,#c7cfd6 0%,#7f8a74 45%,#4f5a3e 100%)}

.reviews{position:absolute;top:1531px;left:0;width:1200px;text-align:center}
.reviews h2{margin-top:60px;font-size:41px;font-weight:600}
.avatar{position:absolute;left:545px;top:136px;width:126px;height:126px;border-radius:50%;border:6px solid #fff;box-shadow:0 0 0 1px #ddd,0 2px 10px rgba(0,0,0,.12);background:radial-gradient(circle at 50% 45%,#b98a6e,#8c3b30)}
.quote-badge{position:absolute;left:643px;top:147px;width:35px;height:35px;border-radius:50%;background:var(--ink);color:#fff;font-size:26px;font-weight:700;line-height:42px}
.rev-arrow{position:absolute;top:248px;width:52px;height:46px;border:1px solid #ccc;display:flex;align-items:center;justify-content:center}
.rev-arrow.prev{left:143px}.rev-arrow.next{right:151px}
.reviews blockquote{position:absolute;left:300px;top:291px;width:600px;font-size:13.5px;font-weight:300;line-height:27px;color:var(--text)}
.reviews cite{position:absolute;left:0;width:1200px;top:400px;font-style:normal;font-size:15px;font-weight:600;display:flex;justify-content:center;align-items:center;gap:10px}
.reviews cite::before{content:"";width:13px;height:3px;background:var(--ink)}

.contact{position:absolute;top:2021px;left:0;width:1200px;height:344px;background:linear-gradient(160deg,#2b2b2b,#121212 60%,#1d1d1d)}
.contact h2{position:absolute;left:79px;top:120px;color:#fff;font-size:41px;font-weight:600}
.contact .sub{position:absolute;left:79px;top:175px;color:#ddd;font-size:15px;font-weight:300}
.form{position:absolute;left:571px;top:87px;width:552px;display:grid;grid-template-columns:271px 271px;gap:11px 10px}
.field{height:47px;background:#fff;font-size:13px;color:#666;padding:0 15px;display:flex;align-items:center;font-weight:400}
.submit{grid-column:1/3;height:52px;margin-top:2px;border:1.5px solid #fff;border-radius:26px;color:#fff;font-size:17px;font-weight:600;display:flex;align-items:center;justify-content:center}

.footer{position:absolute;top:2365px;left:0;width:1200px;height:312px;background:var(--footer);color:#ccc}
.foot-brand{position:absolute;left:111px;top:44px;width:180px;text-align:center}
.foot-brand .mark{width:46px;height:46px;background:var(--steel);margin:0 auto 14px}
.foot-brand .name{font-size:13px;font-weight:600;letter-spacing:2px;color:#aaa;white-space:nowrap}
.socials{position:absolute;left:126px;top:152px;display:flex;gap:7px}
.socials span{width:46px;height:46px;border-radius:50%;border:1.5px solid #ddd}
.col{position:absolute;top:38px}
.col h3{color:#fff;font-size:17px;font-weight:600;margin-bottom:22px}
.col li{font-size:13px;font-weight:300;height:35px;display:flex;align-items:flex-start;gap:10px}
.col.bullets li::before{content:"";width:5px;height:5px;border-radius:50%;background:#fff;margin-top:6px;margin-right:6px}
.col.sitemap{left:345px}.col.svc{left:609px}.col.info{left:875px}
.info li{gap:18px}
.info li svg{fill:#fff;flex:none}
.info .addr{height:58px;line-height:24px;margin-top:-6px}
.info .addr svg{margin-top:6px}
.footer .rule{position:absolute;left:79px;right:79px;top:250px;height:1px;background:#333}
.footer .copy{position:absolute;left:0;width:1200px;top:274px;text-align:center;font-size:13px;font-weight:300;color:#aaa}
.footer .copy b{color:#fff;font-weight:700}
</style>
</head>
<body>

<div class="topbar">
  <div class="item">
    <svg width="17" height="17" viewBox="0 0 24 24"><path d="M6.6 10.8a15.1 15.1 0 0 0 6.6 6.6l2.2-2.2c.3-.3.7-.4 1-.2 1.1.4 2.3.6 3.6.6.6 0 1 .4 1 1V20c0 .6-.4 1-1 1A17 17 0 0 1 3 4c0-.6.4-1 1-1h3.5c.6 0 1 .4 1 1 0 1.3.2 2.5.6 3.6.1.3 0 .7-.2 1z"/></svg>
    <span>123 456 7890</span>
  </div>
  <div class="item">
    <svg width="19" height="15" viewBox="0 0 24 18"><path d="M0 0h24v2L12 9 0 2zM0 4.3l12 7 12-7V18H0z"/></svg>
    <span>info@MaplindRealty.com</span>
  </div>
</div>

<header class="header">
  <div class="brand"><span class="mark"></span><span class="name">MAPLIND REALTY</span></div>
  <nav class="nav">
    <a class="active" href="#">HOME</a>
    <a href="#">ABOUT US</a>
    <a href="#">SERVICES</a>
    <a href="#">CONTACT US</a>
    <span class="search"><svg width="15" height="15" viewBox="0 0 16 16"><circle cx="6.5" cy="6.5" r="5" fill="none" stroke="#111" stroke-width="2"/><path d="M10.2 10.2 15 15" stroke="#111" stroke-width="2.4"/></svg></span>
  </nav>
</header>

<section class="hero" role="img" aria-label="Brownstone townhouse facade on a leafy city street">
  <span class="arrow prev"><svg width="14" height="24" viewBox="0 0 14 24"><path d="M12 2 2 12l10 10" fill="none" stroke="#fff" stroke-width="1.5"/></svg></span>
  <span class="arrow next"><svg width="14" height="24" viewBox="0 0 14 24"><path d="m2 2 10 10L2 22" fill="none" stroke="#fff" stroke-width="1.5"/></svg></span>
  <h1>ASSISTING LANDLORDS<br>INCREASE PROFITS WHILE<br>DECREASING THE STRESS.</h1>
  <a class="btn" href="#">CONTACT US</a>
</section>

<section class="welcome">
  <div class="kicker">WELCOME TO</div>
  <h2>MAPLIND REALITY</h2>
  <p>Maplind Realty AH•CD is a full-service real estate brokerage firm with offices located in Ashford Hill, New York and Coral Dune, Florida. Our firm focuses on multifamily leasing, sales and Commercial Real Estate Site Selection Advisory</p>
  <p>Our clients are private and institutional multifamily real estate investors.<br>Our team differentiates ourselves by our ability to investigate the highest and best use for real estate assets as well as our high deal closing rate.</p>
  <a class="btn" href="#">LEARN MORE</a>
</section>

<section class="services">
  <div class="tile"><div class="photo kitchen" role="img" aria-label="Bright renovated kitchen and dining room"></div><div class="label">MULTI-FAMILY LEASING</div></div>
  <div class="tile"><div class="photo building" role="img" aria-label="Stone multifamily apartment building with fire escapes"></div><div class="label">MULTIFAMILY SALES</div></div>
  <div class="tile"><div class="photo aerial" role="img" aria-label="Aerial view of lakeside land and neighborhoods"></div><div class="label">SITE SELECTION ADVISORS</div></div>
</section>

<section class="reviews">
  <h2>WHAT OUR CLIENT SAY</h2>
  <div class="avatar" role="img" aria-label="Client portrait photo"></div>
  <div class="quote-badge">“</div>
  <span class="rev-arrow prev"><svg width="30" height="12" viewBox="0 0 30 12"><path d="M29 6H2M7 1 2 6l5 5" fill="none" stroke="#aaa" stroke-width="1"/></svg></span>
  <span class="rev-arrow next"><svg width="30" height="12" viewBox="0 0 30 12"><path d="M1 6h27M23 1l5 5-5 5" fill="none" stroke="#aaa" stroke-width="1"/></svg></span>
  <blockquote>" Lorem Ipsum is simply dummy text of the printing and typesetting industry. Lorem Ipsum has been the industry's standard dummy text ever since the 1500s, when an unknown printer took a galley of type and scrambled it to make "</blockquote>
  <cite>CLIENT NAME</cite>
</section>

<section class="contact" role="img" aria-label="Dark photo of hands typing on a laptop">
  <h2>CONTACT US</h2>
  <div class="sub">If you want more info or just to say hello !</div>
  <div class="form">
    <div class="field">Name *</div>
    <div class="field">Email *</div>
    <div class="field">Subject *</div>
    <div class="field">Message *</div>
    <div class="submit">SUBMIT</div>
  </div>
</section>

<footer class="footer">
  <div class="foot-brand"><div class="mark"></div><div class="name">MAPLIND REALTY</div></div>
  <div class="socials"><span></span><span></span><span></span></div>

  <div class="col bullets sitemap">
    <h3>SITEMAP</h3>
    <ul><li>Home</li><li>About Us</li><li>Services</li><li>Contact Us</li></ul>
  </div>
  <div class="col bullets svc">
    <h3>SERVICES</h3>
    <ul><li>Multi-Family Leasing</li><li>Multi-Family Sales</li><li>Site Selection Advisory</li></ul>
  </div>
  <div class="col info">
    <h3>CONTACT US</h3>
    <ul>
      <li class="addr"><svg width="16" height="24" viewBox="0 0 16 24"><path d="M8 0a8 8 0 0 0-8 8c0 6 8 16 8 16s8-10 8-16a8 8 0 0 0-8-8zm0 11a3 3 0 1 1 0-6 3 3 0 0 1 0 6z"/></svg><span>101 - Lorem ipsum simple<br>printing type text print.</span></li>
      <li><svg width="18" height="18" viewBox="0 0 24 24"><path d="M6.6 10.8a15.1 15.1 0 0 0 6.6 6.6l2.2-2.2c.3-.3.7-.4 1-.2 1.1.4 2.3.6 3.6.6.6 0 1 .4 1 1V20c0 .6-.4 1-1 1A17 17 0 0 1 3 4c0-.6.4-1 1-1h3.5c.6 0 1 .4 1 1 0 1.3.2 2.5.6 3.6.1.3 0 .7-.2 1z"/></svg><span>123 456 7890</span></li>
      <li><svg width="19" height="15" viewBox="0 0 24 18"><path d="M0 0h24v2L12 9 0 2zM0 4.3l12 7 12-7V18H0z"/></svg><span>info@MaplindRealty.com</span></li>
    </ul>
  </div>

  <div class="rule"></div>
  <div class="copy">©<b>MAPLIND REALITY</b> - 2019 All Right Reserved.</div>
</footer>

</body>
</html>
```